business card and flyer/pricelist

Business Name: Fern Locks Westbrook
new boutique salon run from home, using Australian owned natural products and colours, we need a flyer design to do a letter box drop to advertise the business as well as incorporating a price list on the front (single sided with writing on front and only colour on back)

The salon has a natural feel with light coloured timber chairs, bamboo timber bench top and shelving.

we are after a natural toned colour for the flyer, with possibly a brown/darkish colour writing

we are after a flyer that will also be able to use the design heading (business name) for business cards as well

feel free to look on my pintrest account to get a feel for my style under Marla Quenby.

I love simple clean and Natural looks.

Font styles to use
Script
Other font styles liked:
• SCRIPT HANDWRITTEN FONTS

Colors
cadf82
e9f1ce
5c5c5c
d3d3d3
add136
fee18a

Requirements
Must have
• NATURAL COLOURINGS, eg soft greens, browns,
white or off white background.
Should not have
• photos,

```html
<!DOCTYPE html>
<html lang="en">
<head>
<meta charset="utf-8">
<title>Fern Locks Westbrook – Price List</title>
<link rel="stylesheet" href="https://fonts.googleapis.com/css2?family=Roboto+Condensed:wght@700&family=Open+Sans:wght@500;600&family=Kaushan+Script&display=swap">
<style>
  :root {
    --espresso: #4a2212;
    --chocolate: #5e2c17;
    --tan: #a86a45;
    --peach-light: #fbe6d2;
    --peach: #f3c8a4;
    --hero-top: #9c9c9c;
    --hero-bottom: #4a4a4a;
    --ink: #4b2414;
    --rule: #c9a188;
    --badge: #b3191c;
    --white: #ffffff;
    --card: #fbf8f5;
  }
  html, body {
    margin: 0;
    padding: 0;
    overflow: hidden;
  }
  body {
    width: 1200px;
    height: 2609px;
    background: var(--white);
  }
  .flyer {
    position: relative;
    width: 1200px;
    height: 2609px;
    overflow: hidden;
    background: linear-gradient(180deg, var(--peach-light) 30%, var(--peach) 100%);
    font-family: "Open Sans", sans-serif;
    color: var(--ink);
  }
  .hero-photo {
    position: absolute;
    left: 0; top: 0;
    width: 1200px; height: 1000px;
    background: radial-gradient(ellipse at 40% 35%, #b9b9b9 0%, var(--hero-top) 35%, var(--hero-bottom) 100%);
  }
  .waves {
    position: absolute;
    left: 0; top: 0;
    width: 1200px; height: 2609px;
  }
  .brand {
    position: absolute;
    right: 58px;
    top: 305px;
    margin: 0;
    text-align: right;
    font-family: "Roboto Condensed", sans-serif;
    font-weight: 700;
    color: var(--white);
    line-height: 1.02;
  }
  .brand .brand-line-1 { display: block; font-size: 84px; }
  .brand .brand-line-2 { display: block; font-size: 58px; }
  .photo-tile {
    position: absolute;
    box-sizing: border-box;
    transform: rotate(45deg);
    border-radius: 30%;
    background: var(--white);
    border: 16px solid var(--chocolate);
    box-shadow: 0 0 0 5px var(--white) inset;
  }
  .photo-tile span {
    position: absolute;
    inset: 10px;
    border-radius: 28%;
  }
  .tile-salon { left: 430px; top: 673px; width: 290px; height: 290px; }
  .tile-salon span { background: linear-gradient(135deg, #d8c6a4, #9a8063); }
  .tile-brush { left: 872px; top: 646px; width: 240px; height: 240px; }
  .tile-brush span { background: linear-gradient(135deg, #e8d2c0, #8a5a3a); }
  .tile-styling { left: 672px; top: 880px; width: 290px; height: 290px; }
  .tile-styling span { background: linear-gradient(135deg, #c89a72, #3c2a22); }
  .price-tab {
    position: absolute;
    left: 0; top: 1104px;
    width: 482px; height: 87px;
    background: var(--chocolate);
  }
  .price-tab::after {
    content: "";
    position: absolute;
    left: 244px; top: 87px;
    border-left: 18px solid transparent;
    border-right: 18px solid transparent;
    border-top: 20px solid var(--chocolate);
  }
  .price-tab h2 {
    margin: 0;
    position: absolute;
    left: 66px; top: 4px;
    font-family: "Kaushan Script", cursive;
    font-weight: 400;
    font-size: 64px;
    color: var(--white);
    letter-spacing: 1px;
  }
  .price-list {
    position: absolute;
    left: 148px; top: 1256px;
    width: 883px;
    margin: 0; padding: 0;
    list-style: none;
  }
  .price-list li {
    position: relative;
    height: 81.7px;
    box-sizing: border-box;
    border-bottom: 2px solid var(--rule);
    display: flex;
    align-items: center;
    font-size: 38px;
    font-weight: 500;
    padding-bottom: 4px;
  }
  .price-list .price {
    margin-left: auto;
    font-weight: 600;
  }
  .badge-new {
    position: absolute;
    left: 440px;
    top: 20px;
    height: 38px;
    padding: 0 22px 0 26px;
    background: var(--badge);
    color: var(--white);
    font-size: 24px;
    line-height: 38px;
    clip-path: polygon(12px 0, 100% 0, 100% 100%, 12px 100%, 0 50%);
  }
  .stylist {
    position: absolute;
    left: 643px; top: 2296px;
    margin: 0;
    font-weight: 500;
    font-size: 50px;
    line-height: 1.05;
    color: var(--chocolate);
  }
  .stylist span { display: block; }
  .stylist .surname { padding-left: 92px; }
  .contact {
    position: absolute;
    left: 362px; top: 2446px;
    margin: 0; padding: 0;
    list-style: none;
    font-size: 26px;
    font-weight: 500;
    color: var(--espresso);
  }
  .contact li {
    display: flex;
    align-items: center;
    height: 43.5px;
  }
  .contact svg { width: 28px; height: 28px; margin-right: 14px; fill: var(--espresso); }
  .contact .fax { margin-left: 28px; }
</style>
</head>
<body>
<main class="flyer">
  <div class="hero-photo" role="img" aria-label="Portrait photo of a model with voluminous tousled dark hair on a grey studio backdrop"></div>

  <svg class="waves" viewBox="0 0 1200 2609" aria-hidden="true">
    <path d="M0,520 C160,760 300,960 470,955 C590,950 610,640 760,590 C900,545 1080,520 1200,505 L1200,2609 L0,2609 Z" fill="var(--chocolate)"/>
    <path d="M0,560 C160,790 300,985 470,982 C600,978 630,680 780,630 C920,585 1090,565 1200,555 L1200,2609 L0,2609 Z" fill="var(--tan)"/>
    <path d="M0,600 C160,820 300,1010 470,1008 C610,1005 650,720 800,670 C940,625 1100,605 1200,598 L1200,2609 L0,2609 Z" fill="url(#peachFill)"/>
    <defs>
      <linearGradient id="peachFill" x1="0" y1="0" x2="0" y2="1">
        <stop offset="0.2" stop-color="#fbe6d2"/>
        <stop offset="1" stop-color="#f1c29c"/>
      </linearGradient>
    </defs>
    <path d="M0,2470 C260,2300 640,2190 1200,2235 L1200,2609 L0,2609 Z" fill="var(--chocolate)"/>
    <path d="M0,2530 C300,2360 680,2255 1200,2285 L1200,2609 L0,2609 Z" fill="var(--tan)"/>
    <path d="M120,2609 C360,2420 720,2300 1200,2325 L1200,2609 Z" fill="var(--card)"/>
    <path d="M0,2609 L0,2590 C40,2570 80,2560 120,2609 Z" fill="var(--chocolate)"/>
  </svg>

  <h1 class="brand"><span class="brand-line-1">Fern Locks</span><span class="brand-line-2">Westbrook</span></h1>

  <div class="photo-tile tile-salon"><span role="img" aria-label="Photo of the salon interior with styling chairs and mirrors"></span></div>
  <div class="photo-tile tile-brush"><span role="img" aria-label="Photo of a client brushing long straight hair"></span></div>
  <div class="photo-tile tile-styling"><span role="img" aria-label="Photo of a stylist cutting a client's hair"></span></div>

  <div class="price-tab"><h2>Price List</h2></div>

  <ul class="price-list">
    <li>Stylish Haircut for Women<span class="price">$49.00</span></li>
    <li>Stylish Haircut for Men<span class="price">$39.00</span></li>
    <li>Stylish Haircut for Kids<span class="price">$39.00</span></li>
    <li>Hair Color / Full Head<span class="price">$69.00</span></li>
    <li>Hair Color / Highlights<span class="price">$79.00</span></li>
    <li>Hair Theropy Treatment<span class="price">$99.00</span></li>
    <li>Hair Wash Only<span class="price">$29.00</span></li>
    <li>Manicure &amp; Spa Pedicure<span class="price">$149.00</span></li>
    <li>Nail Polish Change Hand/Feet<span class="price">$25.00</span></li>
    <li>French Spa Pedcure<span class="badge-new">New</span><span class="price">$125.00</span></li>
    <li>Creative Nail Designs<span class="badge-new">New</span><span class="price">$49.00</span></li>
  </ul>

  <p class="stylist"><span>Delia</span><span class="surname">Marchetti</span></p>

  <ul class="contact">
    <li>
      <svg viewBox="0 0 24 24" aria-hidden="true"><path d="M12 2a7 7 0 0 0-7 7c0 5.2 7 13 7 13s7-7.8 7-13a7 7 0 0 0-7-7zm0 9.6A2.6 2.6 0 1 1 12 6.4a2.6 2.6 0 0 1 0 5.2z"/></svg>
      48 B2/7D, Wattle Par, Heron Road Kelvin, Westbrook City
    </li>
    <li>
      <svg viewBox="0 0 24 24" aria-hidden="true"><rect x="3" y="3" width="18" height="18" rx="3"/><path d="M9 7c-1 0-2 1-1.6 2.6 1 3.4 3.6 6 7 7C16 17 17 16 17 15l-2-1.6-1.4 1c-1.6-.8-2.8-2-3.6-3.6l1-1.4z" fill="#fbf8f5"/></svg>
      (1800) 4312 7785
      <svg class="fax" viewBox="0 0 24 24" aria-hidden="true"><path d="M3 10c0-3 4-5 9-5s9 2 9 5l-3 1-1-2H7L6 11zM6 12h12l2 8H4z"/></svg>
      (Fax) 0912 3344 58
    </li>
    <li>
      <svg viewBox="0 0 24 24" aria-hidden="true"><path d="M2 5h20v14H2zm2 2v.5l8 5.5 8-5.5V7z"/></svg>
      info@fernlockswestbrook.com.au
    </li>
  </ul>
</main>
</body>
</html>
```